Family Psychologist Needs a Sign Designed - Logo Supplied

I am looking for signage on the front window that is bright and catches people’s eyes as they drive past. Therefore, the writing can’t be too small that it is too hard to focus on and read from a moving car.

I want to maybe incorporate the floating spots somehow. I am also looking to hang a banner over the side of the front railing that lists what services are offered since the name doesn’t exactly cover it all . Services include: Psychology, Speech, OT. There is also an education component to the business where we do Study Skills Coaching to high school kids. I would like to see an option of this incorporated to but in a separate way so it isn’t associated with the “psychology” part of the business as this may deter people.

I also want to put a sign above the business in the overhead light thing (not sure what its called). Currently it is empty but the clinics next door have “chiropractor” and “medical centre” written in theirs so mine will have to be as equally simple but specific. Logo attached (EPS)

Ive also attached my logo and a few examples of where the signagewill go.

```html
<!DOCTYPE html>
<html lang="en">
<head>
<meta charset="utf-8">
<title>Clear Path – Shopfront Signage</title>
<link rel="stylesheet" href="https://fonts.googleapis.com/css2?family=Source+Sans+3:wght@400;700&family=Cormorant+Garamond:ital,wght@1,500&display=swap">
<style>
  :root {
    --page: #ffffff;
    --wall: #e6e7e8;
    --frame: #1b1b1b;
    --glass-dark: #4d4d4f;
    --glass-light: #7b7c7e;
    --panel: #ffffff;
    --silver: #b9bbbe;
    --lime: #c5dc4a;
    --green: #8cc63f;
    --teal: #2fa89a;
    --cyan: #3cc3d6;
    --brand: #2aa79b;
    --tagline: #2b7fc1;
    --ink-white: #ffffff;
  }
  html, body {
    margin: 0;
    padding: 0;
    width: 1200px;
    height: 570px;
    overflow: hidden;
    background: var(--page);
  }
  .shopfront { display: block; width: 1200px; height: 570px; }
  .brand-name { font-family: "Source Sans 3", sans-serif; font-weight: 700; fill: var(--brand); }
  .brand-tagline { font-family: "Source Sans 3", sans-serif; font-weight: 400; fill: var(--tagline); }
  .service-label { font-family: "Source Sans 3", sans-serif; font-weight: 700; fill: var(--ink-white); }
  .slogan { font-family: "Cormorant Garamond", serif; font-style: italic; font-weight: 500; fill: var(--teal); }
  .coaching-line { font-family: "Source Sans 3", sans-serif; font-weight: 700; fill: var(--ink-white); }
  .frame { fill: var(--frame); }
  .glass { fill: url(#glass-tone); }
  .panel { fill: var(--panel); stroke: var(--silver); stroke-width: 5; }
  .band-fill { fill: url(#band-tone); }
  .door-fill { fill: url(#door-tone); }
  .edge-white { fill: none; stroke: var(--ink-white); }
  .edge-dark { fill: none; stroke: var(--frame); }
  .edge-teal { fill: none; stroke: var(--cyan); }
  .brand-square { fill: var(--teal); }
  .louvre { stroke: var(--frame); stroke-width: 3; }
  .mullion { fill: var(--frame); }
</style>
</head>
<body>
<svg class="shopfront" viewBox="0 0 1200 570" xmlns="http://www.w3.org/2000/svg" aria-label="Clear Path shopfront signage">
  <defs>
    <linearGradient id="glass-tone" x1="0" y1="0" x2="1" y2="1">
      <stop offset="0" stop-color="#4d4d4f"/>
      <stop offset="0.5" stop-color="#7b7c7e"/>
      <stop offset="1" stop-color="#4d4d4f"/>
    </linearGradient>
    <linearGradient id="band-tone" x1="0" y1="0" x2="1" y2="0">
      <stop offset="0" stop-color="#c5dc4a"/>
      <stop offset="0.5" stop-color="#3fae8e"/>
      <stop offset="1" stop-color="#3cc3d6"/>
    </linearGradient>
    <linearGradient id="door-tone" x1="0" y1="0" x2="1" y2="0">
      <stop offset="0" stop-color="#d9e66e"/>
      <stop offset="1" stop-color="#b5d650"/>
    </linearGradient>
    <linearGradient id="services-tone" x1="0" y1="0" x2="1" y2="1">
      <stop offset="0" stop-color="#8cc63f"/>
      <stop offset="1" stop-color="#79b93a"/>
    </linearGradient>
    <linearGradient id="spots-tone" x1="0" y1="0" x2="0" y2="1">
      <stop offset="0" stop-color="#ffffff" stop-opacity="0.55"/>
      <stop offset="1" stop-color="#ffffff" stop-opacity="0.1"/>
    </linearGradient>
  </defs>

  <!-- Entry doors -->
  <g class="entry-doors">
    <rect class="frame" x="52" y="42" width="318" height="460"/>
    <rect class="glass" x="58" y="48" width="306" height="36" opacity="0.8"/>
    <rect class="glass" x="58" y="122" width="178" height="375"/>
    <rect class="glass" x="250" y="122" width="118" height="375"/>
    <g role="img" aria-label="Soft lime window film across the lower doors">
      <path class="door-fill" d="M58 292 Q150 318 236 316 L236 497 L58 497Z"/>
      <path class="door-fill" d="M250 314 Q310 308 368 298 L368 497 L250 497Z"/>
    </g>
    <path class="edge-white" stroke-width="8" d="M58 287 Q200 322 368 294"/>
    <rect x="233" y="265" width="4" height="30" fill="#d0d0d0"/>
    <rect x="241" y="265" width="4" height="30" fill="#d0d0d0"/>

    <g class="door-brand">
      <rect class="brand-square" x="90" y="212" width="30" height="30"/>
      <text class="brand-name" x="126" y="236" font-size="22">CLEAR PATH</text>
      <text class="brand-tagline" x="126" y="252" font-size="9">Psychology &amp; Education</text>
    </g>
    <g class="door-brand">
      <rect class="brand-square" x="274" y="212" width="30" height="30"/>
      <text class="brand-name" x="308" y="236" font-size="22">CLEAR PATH</text>
      <text class="brand-tagline" x="308" y="252" font-size="9">Psychology &amp; Education</text>
    </g>
  </g>

  <!-- Shop window -->
  <g class="shop-window">
    <rect x="370" y="42" width="818" height="498" fill="var(--wall)"/>
    <rect class="glass" x="437" y="42" width="751" height="451"/>
    <rect class="mullion" x="610" y="172" width="6" height="321"/>
    <rect class="mullion" x="798" y="172" width="6" height="321"/>
    <rect class="mullion" x="998" y="172" width="6" height="321"/>

    <path class="band-fill" role="img" aria-label="Soft green to cyan window film band" d="M437 292 Q620 205 820 222 Q1000 236 1188 270 L1188 493 L437 493Z"/>
    <path class="edge-white" stroke-width="14" d="M437 282 Q620 195 820 212 Q1000 226 1188 260"/>
    <rect class="frame" x="437" y="293" width="751" height="4"/>

    <rect x="555" y="176" width="135" height="144" rx="20" fill="url(#spots-tone)" role="img" aria-label="Floating spots decoration"/>

    <g class="louvres">
      <line class="louvre" x1="445" y1="330" x2="520" y2="330"/>
      <line class="louvre" x1="445" y1="352" x2="520" y2="352"/>
      <line class="louvre" x1="445" y1="374" x2="520" y2="374"/>
      <line class="louvre" x1="445" y1="396" x2="520" y2="396"/>
      <line class="louvre" x1="445" y1="418" x2="520" y2="418"/>
      <line class="louvre" x1="445" y1="440" x2="520" y2="440"/>
      <line class="louvre" x1="445" y1="462" x2="520" y2="462"/>
      <line class="louvre" x1="445" y1="484" x2="520" y2="484"/>
      <line class="louvre" x1="1100" y1="330" x2="1165" y2="330"/>
      <line class="louvre" x1="1100" y1="352" x2="1165" y2="352"/>
      <line class="louvre" x1="1100" y1="374" x2="1165" y2="374"/>
      <line class="louvre" x1="1100" y1="396" x2="1165" y2="396"/>
      <line class="louvre" x1="1100" y1="418" x2="1165" y2="418"/>
      <line class="louvre" x1="1100" y1="440" x2="1165" y2="440"/>
      <line class="louvre" x1="1100" y1="462" x2="1165" y2="462"/>
      <line class="louvre" x1="1100" y1="484" x2="1165" y2="484"/>
    </g>
  </g>

  <!-- Overhead services sign -->
  <g class="services-sign">
    <rect class="panel" x="507" y="50" width="610" height="120"/>
    <path class="band-fill" role="img" aria-label="Soft green to cyan band" d="M512 150 Q640 105 760 118 Q900 132 1112 138 L1112 166 L512 166Z"/>
    <path class="edge-dark" stroke-width="4" d="M512 146 Q640 100 760 113 Q900 127 1112 132"/>
    <rect x="552" y="55" width="212" height="70" rx="14" fill="url(#services-tone)" role="img" aria-label="Floating spots behind the service names"/>
    <text class="service-label" x="588" y="78" font-size="13" text-anchor="middle">SPEECH</text>
    <text class="service-label" x="718" y="96" font-size="13" text-anchor="middle">Phychology</text>
    <text class="service-label" x="610" y="112" font-size="11" text-anchor="middle">Skills</text>
    <text class="service-label" x="662" y="114" font-size="17" text-anchor="middle">OT</text>
    <text class="brand-name" x="1055" y="84" font-size="24" text-anchor="middle">CLEAR</text>
    <text class="brand-name" x="1055" y="112" font-size="24" text-anchor="middle">PATH</text>
  </g>

  <!-- Window banner -->
  <g class="window-banner">
    <rect class="panel" x="520" y="320" width="578" height="170"/>
    <path class="band-fill" role="img" aria-label="Soft green to cyan band" d="M525 452 Q700 420 820 432 Q960 446 1093 410 L1093 486 L525 486Z"/>
    <path class="edge-dark" stroke-width="4" d="M525 448 Q700 416 820 428 Q960 442 1093 406"/>
    <rect class="brand-square" x="550" y="358" width="36" height="36"/>
    <text class="brand-name" x="594" y="388" font-size="28">CLEAR PATH</text>
    <text class="brand-tagline" x="594" y="406" font-size="11">Multiclinic &amp; Education</text>
    <text class="slogan" x="925" y="367" font-size="30" text-anchor="middle">Helping you see a</text>
    <text class="slogan" x="925" y="404" font-size="30" text-anchor="middle">brighter future!</text>
    <text class="coaching-line" x="905" y="481" font-size="15" text-anchor="middle">Ask about our study skills coaching for students</text>
  </g>
</svg>
</body>
</html>
```